Guarding One's Body Using Sharp Steel Cover

Hi we are producing a self defense course entitled Guarding One's Body Using Sharp Steel: A Complete Manual For Learning The Finest And Handiest Wilderness Tool In Recorded History.

I listed this as a book cover but it will actually be a DVD set, but the book cover model works fine.

See below for design examples - I am thinking we need a cover that will appeal to military/survival type people.

Target Market(s)

survivalists, cops, preppers, gun owners, martial artists, and average people wanting to learn how to defend themselves

Industry/Entity Type

Defense

Requirements
Must have
• Title: GUARDING ONE'S BODY USING SHARP STEEL: A COMPLETE MANUAL FOR LEARNING THE FINEST AND HANDIEST WILDERNESS TOOL IN RECORDED HISTORY
Nice to have
• Please look at these sample designs from other books as a model:
• https://files.plorvexa.org/media/en/4/27/BrindelQXMP.jpg - This stye is ideal.
• Other good examples:
• https://pics2.talvorn.com/8143907_k370.jpg
• http://m.zephquill.com/titles/2719058463k/48071935.jpg
• http://img.crondelmart.com/pics/P/73Tm58QyzFr._BX_KL410_TR316,410_.jpg
• http://3.cdn.wendoplix.net/-RTyZWLMMKAQ/BNWq_hufxaT/BBBBBBBBv8G/DKNp815ZaXW/s1600/Q4710392.JPG

```html
<!DOCTYPE html>
<html lang="en">
<head>
<meta charset="utf-8">
<title>Guarding One's Body Using Sharp Steel – Cover</title>
<link rel="stylesheet" href="https://fonts.googleapis.com/css2?family=Montserrat:wght@900&family=Bebas+Neue&family=Oswald:wght@500;700&display=swap">
<style>
  :root {
    --stage: #d9d6d2;
    --cover-deep: #1c1730;
    --cover-mid: #3a2346;
    --ember: rgba(232, 87, 44, 0.55);
    --violet: rgba(150, 60, 140, 0.35);
    --art-top: rgba(70, 26, 40, 0);
    --art-mid: rgba(74, 28, 42, 0.75);
    --art-low: rgba(44, 22, 46, 0.9);
    --title-white: #ffffff;
    --title-red: #e8232d;
    --bone: #f1e4d2;
    --author-red: #b8312c;
  }
  html, body {
    margin: 0;
    width: 1001px;
    height: 1200px;
    overflow: hidden;
    background: var(--stage);
  }
  .canvas {
    position: relative;
    width: 1001px;
    height: 1200px;
  }
  .cover {
    position: absolute;
    left: 170px;
    top: 20px;
    width: 660px;
    height: 1160px;
    overflow: hidden;
    background:
      radial-gradient(ellipse 60% 30% at 45% 25%, var(--ember), transparent 70%),
      radial-gradient(ellipse 70% 40% at 30% 55%, var(--violet), transparent 75%),
      linear-gradient(180deg, var(--cover-mid) 0%, var(--cover-deep) 60%, #15112a 100%);
    box-shadow: 0 10px 30px rgba(0,0,0,0.25);
  }
  .cover-art {
    position: absolute;
    left: 0;
    top: 430px;
    width: 100%;
    height: 730px;
    background: linear-gradient(180deg, var(--art-top) 0%, var(--art-mid) 30%, var(--art-low) 100%);
  }
  .rule {
    position: absolute;
    left: 0;
    width: 100%;
    height: 4px;
    background: var(--title-white);
  }
  .rule--top { top: 63px; }
  .rule--middle { top: 456px; }
  .rule--lower { top: 570px; }
  .title { margin: 0; }
  .title__lead {
    position: absolute;
    left: 30px;
    top: 82px;
    font-family: "Montserrat", sans-serif;
    font-weight: 900;
    font-size: 64px;
    line-height: 0.86;
    letter-spacing: -2px;
    color: var(--title-white);
    text-transform: uppercase;
    white-space: nowrap;
  }
  .title__main {
    position: absolute;
    left: 30px;
    top: 255px;
    font-family: "Bebas Neue", sans-serif;
    font-weight: 400;
    font-size: 126px;
    line-height: 1;
    color: var(--title-red);
    transform: scaleY(2.25);
    transform-origin: top left;
    white-space: nowrap;
  }
  .subtitle {
    position: absolute;
    left: 58px;
    right: 50px;
    top: 730px;
    display: grid;
    grid-template-columns: auto auto auto;
    justify-content: center;
    align-items: end;
    color: var(--bone);
    font-family: "Oswald", sans-serif;
    font-weight: 700;
    text-transform: uppercase;
    line-height: 0.92;
  }
  .subtitle .s { display: block; font-size: 26px; }
  .subtitle .l { display: block; font-size: 58px; }
  .subtitle .m { display: block; font-size: 36px; }
  .subtitle__right { padding-left: 4px; }
  .subtitle__amp {
    font-size: 110px;
    line-height: 0.8;
    color: var(--author-red);
    padding-left: 6px;
  }
  .author {
    position: absolute;
    left: 50px;
    right: 30px;
    top: 1060px;
    margin: 0;
    font-family: "Oswald", sans-serif;
    font-weight: 500;
    font-size: 28px;
    letter-spacing: 20px;
    color: var(--author-red);
    text-transform: uppercase;
    white-space: nowrap;
  }
</style>
</head>
<body>
<main class="canvas">
  <article class="cover">
    <div class="cover-art" role="img" aria-label="Photo area: silhouette of a man in a cap against a glowing cracked backdrop"></div>
    <div class="rule rule--top"></div>
    <div class="rule rule--middle"></div>
    <div class="rule rule--lower"></div>
    <h1 class="title">
      <span class="title__lead">Guarding One's<br>Body Using</span>
      <span class="title__main">SHARP STEEL</span>
    </h1>
    <div class="subtitle">
      <div class="subtitle__left">
        <span class="s">A Complete</span>
        <span class="l">Manual</span>
        <span class="s">For Learning</span>
        <span class="m">The Finest</span>
      </div>
      <div class="subtitle__amp">&amp;</div>
      <div class="subtitle__right">
        <span class="m">Handiest</span>
        <span class="m">Wilderness</span>
        <span class="s">Tool In Recorded</span>
        <span class="l">History</span>
      </div>
    </div>
    <p class="author">Dorian Valcrest</p>
  </article>
</main>
</body>
</html>
```